Design a book cover for "The Harvester's Ledger"

We need a book cover for a book titled "The Harvester's Ledger" The subtitle is "Why Machines Deliver a Shared Dividend, the Close of Levy Systems, and a Steady Treasury"
You can use one of the attached files of cover art, or come up with your own art - designer's choice!
Author's Name is Brent Hallow
We'd like the copy in the attached file "Back Cover" on the back cover, along with the copy in "About the Author" and the author's photo on the back cover.
Updates

Project Deadline Extended Reason: The deadline has been extended to give time for designers to respond to comments. Feel free to submit designs that do not use the cover art graphics attached to the brief - that art was meant as a suggestion. Added Sunday, January 15, 2017

Target Market(s)

Layperson

Font styles to use
Sans Serif

Colors
0456a4
3176b5
85abd2
0293ce
33a6d7
85cae6
1b1b1b
474747
919191

Requirements
Nice to have
• We'd like to see how the horse and rider would look on the front cover. The attached file, "Pendlewick Option", is a rough sketch. The artist is refining it, adding color, and will have the rider carrying modern technology instead of scrolls.
• We are open to all colors, but have indicated some colors we like.

```html
<!DOCTYPE html>
<html lang="en">
<head>
<meta charset="utf-8">
<title>The Harvester's Ledger — Book Cover</title>
<link href="https://fonts.googleapis.com/css2?family=Arvo:wght@700&family=Open+Sans:ital,wght@0,400;0,600;0,700;1,400&display=swap" rel="stylesheet">
<style>
  :root {
    --stage: #6f6f6f;
    --cover-deep: #174f6e;
    --cover-mid: #1f6587;
    --cover-glow: #4fa3c6;
    --text-light: #ffffff;
    --text-soft: #e3eef4;
    --photo-tone: #8a6a52;
    --photo-frame: #dfe7ec;
  }
  * { box-sizing: border-box; margin: 0; padding: 0; }
  html, body {
    width: 1200px; height: 800px; overflow: hidden;
    background: var(--stage);
  }
  .canvas {
    position: relative; width: 1200px; height: 800px;
    display: flex; justify-content: center; align-items: center; gap: 40px;
  }
  .cover {
    position: relative; width: 360px; height: 540px;
    background: radial-gradient(ellipse at 50% 45%, var(--cover-mid) 0%, var(--cover-deep) 75%);
    box-shadow: 0 10px 30px rgba(0,0,0,0.35);
    overflow: hidden;
    font-family: "Open Sans", sans-serif;
    color: var(--text-light);
  }
  /* Front */
  .front-title {
    position: absolute; top: 30px; left: 0; right: 0;
    text-align: center;
    font-family: "Arvo", serif; font-weight: 700; font-size: 26px;
    letter-spacing: 0.2px;
  }
  .front-art {
    position: absolute; top: 80px; left: 20px; width: 320px; height: 320px;
    border-radius: 50%;
    background: radial-gradient(circle at 50% 52%, #eef5f8 0%, #b9d9e6 14%, var(--cover-glow) 32%, var(--cover-mid) 58%, rgba(31,101,135,0) 72%);
  }
  .front-subtitle {
    position: absolute; bottom: 26px; left: 16px; right: 16px;
    text-align: center; font-size: 13.5px; line-height: 1.4;
  }
  /* Back */
  .back-copy {
    position: absolute; top: 62px; left: 42px; right: 36px;
    font-size: 11px; line-height: 1.42; color: var(--text-soft);
  }
  .back-copy p + p { margin-top: 12px; }
  .back-copy .lead-title { font-size: 16px; color: var(--text-light); }
  .author {
    position: absolute; top: 372px; left: 42px; right: 30px;
    display: flex; gap: 10px;
  }
  .author-photo {
    flex: none; width: 74px; height: 92px;
    border: 2px solid var(--photo-frame);
    background: linear-gradient(160deg, #6d8a5a 0%, var(--photo-tone) 55%, #7a2a2a 100%);
  }
  .author-heading { font-size: 9.5px; font-weight: 700; margin-bottom: 3px; }
  .author-bio { font-size: 7.6px; line-height: 1.45; font-style: italic; color: var(--text-soft); }
</style>
</head>
<body>
  <main class="canvas">
    <section class="cover cover-front">
      <h1 class="front-title">The Harvester's Ledger</h1>
      <div class="front-art" role="img" aria-label="Cover artwork: a white cloud at the centre of a glowing circular circuit pattern with small currency coins"></div>
      <p class="front-subtitle">Why Machines Deliver a Shared Dividend,<br>the Close of Levy Systems, and a Steady Treasury</p>
    </section>

    <section class="cover cover-back">
      <div class="back-copy">
        <p><span class="lead-title">The Harvester's Ledger</span> is the story of how technology is changing the economy. If we play it right, we can all win. The efficiency of technology, when combined with a new understanding of money, can eliminate the need for income taxes. It can balance the budget, pay off the national debt, and provide a national income for all. It is the basis of free higher education, free healthcare, and the eradication of poverty.</p>
        <p>The solutions that Hallow proposes in The Harvester's Ledger are nonpartisan, benefiting both poor and rich. They would propel our nation to greater heights than it has ever known. It is simply a matter of understanding how technology impacts production, and how the monetary economy can be used to stoke the production engine that technology is building, rather than creating roadblocks to our prosperity as the current system does.</p>
      </div>
      <div class="author">
        <div class="author-photo" role="img" aria-label="Portrait photograph of the author"></div>
        <div class="author-text">
          <h2 class="author-heading">About the Author</h2>
          <p class="author-bio">Brent Hallow spent two decades advising regional banks, later led research for a rural development fund and co-founded two chartered schools. He built a small software firm, taught evening courses in applied economics, and now writes and lectures on money, work, and the future of shared prosperity from his home in the western hills.</p>
        </div>
      </div>
    </section>
  </main>
</body>
</html>
```